Parcelnook.com.au Front page Re-Design

We need a front page redesign for the website parcelnook.com.au,
The site needs to keep a number of products products highlighted on the front page. Same buttons but navigation could be different and we still need some text for SEO.
What we do not currently like:
1. The big banners.
2. The use of too much orange especially the 50% orange borders.
3. the fact that products cannot be seen straight away when logged-in.
4. The fact that it is hard to convert to tablet friendly
5. The fact that it's not a modern design.

What we think we want:

1. Maybe more use of 1 colour (purple or orange) with the other a secondary highlight colour.
2. A more modern look
3. The wow factor

Look at parcelnook.com.au take the elements that you need and design.
Updates

Reason: Designs are getting better. liking the designs that don't look like the usual e-commerce templates out there.

Hello,

We are making decisions next Monday. Sorry for the delay but there has been a lot of holidays in Australia and decision makers away.

Industry/Entity Type

Seo

Colors
6b449b
f78f20
ffffff

```html
<!DOCTYPE html>
<html lang="en">
<head>
<meta charset="utf-8">
<title>Parcelnook.com.au – Front Page</title>
<link href="https://fonts.googleapis.com/css2?family=Open+Sans:wght@400;600;700&display=swap" rel="stylesheet">
<style>
:root{
  --purple:#6b449b;
  --purple-soft:#9a7cc4;
  --orange:#f78f20;
  --white:#ffffff;
  --ink:#333338;
  --grey:#6d6d72;
  --line:#e2e2e6;
  --topbar:#3a3a40;
  --footer:#efefef;
  --pink:#e85a9a;
}
*{box-sizing:border-box;margin:0;padding:0}
html,body{width:758px;height:1200px;overflow:hidden;background:var(--white)}
body{font-family:"Open Sans",Arial,sans-serif;color:var(--ink);position:relative}
.abs{position:absolute}

/* top bar */
.topbar{left:0;top:0;width:758px;height:25px;background:var(--topbar);color:var(--white);font-size:7.5px;display:flex;align-items:center;padding:0 66px 0 68px}
.topbar .welcome{font-weight:600;flex:1}
.topbar .links{display:flex;gap:22px;color:#dcdce0}
.topbar .links span::before{content:"";display:inline-block;width:6px;height:6px;border:1px solid #dcdce0;border-radius:1px;margin-right:3px;vertical-align:-1px}

/* header */
.brand{left:66px;top:36px;display:flex;align-items:center;gap:6px}
.brand .mark{width:22px;height:22px;background:var(--orange);border-radius:3px}
.brand .name{font-size:17px;font-weight:700;color:var(--purple);line-height:1}
.brand-tag{left:69px;top:78px;font-size:7px;color:var(--purple)}
.cart{left:600px;top:48px;display:flex;gap:6px;align-items:center}
.cart .bag{width:17px;height:21px;background:var(--orange);border-radius:2px 2px 4px 4px}
.cart .t1{font-size:8.5px;color:var(--ink)}
.cart .t2{font-size:7px;color:var(--orange)}

/* nav */
.nav{left:62px;top:95px;width:633px;height:34px;background:var(--purple);display:flex;align-items:center;border:1px solid #5a3689}
.nav a{color:var(--white);text-decoration:none;font-size:9.5px;padding:0 10.5px;height:100%;display:flex;align-items:center}
.nav a.active{background:var(--orange);color:#3a2a1a;padding:0 9px}
.search{margin-left:auto;margin-right:6px;width:170px;height:22px;border:1px solid #b9a3d6;display:flex;align-items:center;justify-content:space-between;padding:0 6px;color:#d9cdea;font-size:7px}

/* sidebar */
.side-title{font-size:11px;color:var(--purple);font-weight:400;letter-spacing:.2px}
.cats{left:67px;top:179px;width:141px;list-style:none}
.cats li{height:25.3px;border-bottom:1px solid var(--line);display:flex;align-items:center;justify-content:space-between;font-size:8.5px;color:var(--grey);padding:0 2px}
.cats li::after{content:"";width:5px;height:5px;border-right:1px solid #777;border-top:1px solid #777;transform:rotate(45deg);margin-right:3px}
.seller{left:67px;width:141px;display:flex;gap:8px;height:62px;border-bottom:1px solid var(--line)}
.seller .thumb{width:46px;height:46px;background:linear-gradient(135deg,#eee9e2,#d9d2c8);border:1px solid #ddd}
.seller p{font-size:7px;color:var(--purple);line-height:1.3}
.seller b{display:block;font-size:8px;color:var(--ink);font-weight:400;margin-top:4px}
.promo{left:63px;top:782px;width:146px;height:172px;border:1px solid var(--pink)}
.promo .art{height:144px;background:linear-gradient(160deg,#f6d9e6,#e8b3cb 60%,#cf8aa8)}
.promo .cap{height:26px;background:var(--pink);color:var(--white);font-size:7px;padding:3px 8px;line-height:1.25}
.social{left:65px;top:1005px;display:flex;gap:10px}
.social span{width:21px;height:21px;border-radius:50%;background:var(--purple)}
.social span:nth-child(even){background:var(--orange)}
.news{left:67px;top:1074px;width:144px;height:24px;display:flex;border:1px solid #ccc}
.news .in{flex:1;font-size:7px;color:#999;display:flex;align-items:center;padding-left:7px}
.news .go{width:34px;background:var(--purple);display:flex;align-items:center;justify-content:center}

/* hero */
.hero{left:224px;top:148px;width:471px;height:216px;background:#f1f1f3;border:1px solid var(--line)}
.hero .photo{position:absolute;right:0;top:0;width:230px;height:172px;background:linear-gradient(120deg,#f1f1f3 0%,#e9ddd6 35%,#c89a86 60%,#3d6a5c 100%)}
.hero h1{position:absolute;left:17px;top:34px;font-size:22px;font-weight:400;color:var(--purple);letter-spacing:.5px;line-height:1}
.hero .sub{position:absolute;left:18px;top:59px;font-size:9px;color:var(--ink)}
.hero .desc{position:absolute;left:18px;top:77px;font-size:7.3px;color:var(--ink);width:160px;line-height:1.4}
.hero .btn{position:absolute;left:18px;top:110px;width:97px;height:29px;background:#2c2c30;color:var(--white);font-size:10.5px;display:flex;align-items:center;justify-content:center}
.hero .strip{position:absolute;left:0;bottom:0;width:100%;height:44px;background:var(--purple-soft);display:flex;align-items:center;color:var(--white)}
.strip .big{padding-left:8px;width:155px;line-height:1.05}
.strip .big b{display:block;font-size:17px;color:var(--orange);font-weight:700}
.strip .big span{font-size:15px}
.strip .slash{width:2px;height:38px;background:var(--white);transform:rotate(12deg);margin-right:12px}
.strip .msg{font-size:7px;line-height:1.4;width:290px}
.strip .next{position:absolute;right:28px;top:14px;width:15px;height:15px;border-radius:50%;background:var(--white)}
.strip .next::after{content:"";position:absolute;left:4px;top:5px;width:4px;height:4px;border-right:1px solid #555;border-top:1px solid #555;transform:rotate(45deg)}

/* products */
.sec-title{font-size:11.5px;color:var(--ink);border-bottom:1px solid var(--line);width:465px;padding-bottom:5px}
.grid{left:230px;top:417px;display:grid;grid-template-columns:repeat(4,104px);column-gap:16.3px;row-gap:0}
.card{height:158px}
.card:nth-child(n+5){height:160px}
.card .pic{width:104px;height:104px;border:1px solid #d8d8dc;position:relative}
.card.on .pic{border:1px solid var(--purple)}
.card p{font-size:6.5px;color:var(--grey);margin-top:5px;line-height:1.35;width:100px}
.card .price{font-size:7px;color:var(--purple);margin-top:1px}
.tag{position:absolute;left:6px;top:6px;width:24px;height:24px;border-radius:50%;color:var(--white);font-size:7px;font-style:italic;font-weight:700;display:flex;align-items:center;justify-content:center}
.tag.new{background:#1a9a4a}.tag.sale{background:#1f7fe0}.tag.best{background:#e0266a}
.quick{position:absolute;left:26px;top:40px;width:52px;font-size:6.5px;text-align:center}
.quick .q{background:rgba(255,255,255,.75);color:#555;padding:2px 0}
.quick .a{background:var(--purple);color:var(--white);padding:3px 0;margin-top:4px}
.t-band{background:linear-gradient(135deg,#eeebe8,#d9d3cc)}
.t-hooks{background:linear-gradient(180deg,#eceae7,#c9c0b5 50%,#eceae7)}
.t-cups{background:linear-gradient(90deg,#f1efee,#f2a09a 35%,#9fdcb0 65%,#f1efee)}
.t-basket{background:linear-gradient(135deg,#f3f3f3,#c9424a 60%,#8b6a3a)}
.t-rings{background:linear-gradient(135deg,#dcd6d2,#b49170)}
.t-flower{background:linear-gradient(180deg,#cfcfcf,#f1f1f1)}
.t-eggs{background:linear-gradient(135deg,#f4ece6,#e7c8b4)}

/* about */
.about-img{left:229px;top:941px;width:129px;height:129px;border:1px solid #ccc;background:linear-gradient(135deg,#f2f2f2,#e66a8e 45%,#6fa0c8 75%,#c94f2a)}
.about{left:367px;top:938px;width:325px}
.about h3{font-size:8.7px;font-weight:400;color:var(--ink);margin-bottom:5px}
.about p{font-size:6.5px;color:var(--grey);line-height:1.3;margin-bottom:6px}

/* footer */
.footer{left:0;top:1128px;width:758px;height:72px;background:var(--footer)}
.flinks{left:66px;top:1153px;font-size:7.5px;color:var(--ink);display:flex;gap:5px}
.flinks i{font-style:normal;color:#999}
.copy{left:66px;top:1169px;font-size:7.5px;color:var(--ink)}
.pay{left:569px;top:1148px;display:flex;gap:7px}
.pay span{width:20px;height:11px;border-radius:2px;background:#c9c9d0}
.pay span:last-child{width:28px;background:#b3b3bd}
</style>
</head>
<body>

<div class="abs topbar">
  <div class="welcome">Default welcome msg!</div>
  <div class="links"><span>My Account</span><span>My Wishlist</span><span>My Cart</span><span>Checkout</span><span>Log In</span></div>
</div>

<div class="abs brand"><div class="mark"></div><div class="name">Parcelnook.com.au</div></div>
<div class="abs brand-tag">parcel &amp; hamper network</div>

<div class="abs cart">
  <div class="bag"></div>
  <div><div class="t1">Shopping cart</div><div class="t2">0 item (s) - $ 0.00</div></div>
</div>

<nav class="abs nav">
  <a class="active">HOME</a><a>SHOP BRAND</a><a>UNIQUE</a><a>GIFTS</a><a>SPECIALS</a><a>CUSTOM MENU</a>
  <div class="search">Search Entire Store Here......
    <svg width="11" height="11" viewBox="0 0 12 12"><circle cx="5" cy="5" r="3.8" fill="none" stroke="#fff" stroke-width="1.3"/><line x1="8" y1="8" x2="11" y2="11" stroke="#fff" stroke-width="1.5"/></svg>
  </div>
</nav>

<!-- sidebar -->
<div class="abs side-title" style="left:67px;top:155px">CATEGORIES</div>
<ul class="abs cats">
  <li>Easter</li><li>Mother Day</li><li>Get Well</li><li>Thank You</li><li>Birthday</li><li>Anniversary</li><li>Romance</li><li>New Baby</li><li>Children</li><li>For Her</li><li>For Him</li>
</ul>

<div class="abs side-title" style="left:67px;top:477px">TOP SELLER</div>
<div class="abs seller" style="top:500px"><div class="thumb" role="img" aria-label="Charm bracelet on a plate"></div><div><p>Lorem Ipsum is simply dummy text of the</p><b>$109.66</b></div></div>
<div class="abs seller" style="top:570px"><div class="thumb" role="img" aria-label="Colourful stud earrings"></div><div><p>Lorem Ipsum is simply dummy text of the</p><b>$109.66</b></div></div>
<div class="abs seller" style="top:641px"><div class="thumb" role="img" aria-label="Pendant necklace with bow"></div><div><p>Lorem Ipsum is simply dummy text of the</p><b>$109.66</b></div></div>
<div class="abs seller" style="top:712px;border-bottom:none"><div class="thumb" role="img" aria-label="Beaded bracelet with charms"></div><div><p>Lorem Ipsum is simply dummy text of the</p><b>$109.66</b></div></div>

<div class="abs promo">
  <div class="art" role="img" aria-label="Pink friendship greeting card with wrapping paper"></div>
  <div class="cap">Neque porro quisquam est, qui dolorem ipsum quia dolor sit amet</div>
</div>

<div class="abs side-title" style="left:67px;top:982px">FOLLOW US ON</div>
<div class="abs social"><span></span><span></span><span></span><span></span><span></span></div>

<div class="abs side-title" style="left:67px;top:1049px">NEWSLETTER</div>
<div class="abs news"><div class="in">Email...</div><div class="go">
  <svg width="16" height="8" viewBox="0 0 16 8"><line x1="0" y1="4" x2="15" y2="4" stroke="#fff" stroke-width="1"/><polyline points="11,0.5 15,4 11,7.5" fill="none" stroke="#fff" stroke-width="1"/></svg>
</div></div>

<!-- hero -->
<section class="abs hero">
  <div class="photo" role="img" aria-label="Woman holding a red gift box with a green bow"></div>
  <h1>SPECIAL GIFT</h1>
  <div class="sub">Lorem Ipsum is simply dummy</div>
  <div class="desc">Lorem Ipsum is simply dummy text of the printing and typesetting indus</div>
  <div class="btn">Shope Now</div>
  <div class="strip">
    <div class="big"><b>Gift Baskets</b><span>Hampers Delivered</span></div>
    <div class="slash"></div>
    <div class="msg">Gift Baskets and Hampers great range is now available with Gift Delivery Australia Wide! Send a gift Australia wide today. Fast delivery<br>Gift baskets delivered Australia wide! Gift ideas for Christmas,</div>
    <div class="next"></div>
  </div>
</section>

<!-- products -->
<div class="abs sec-title" style="left:230px;top:382px">New Products</div>
<div class="abs grid">
  <div class="card on"><div class="pic t-band" role="img" aria-label="Charm bracelet on a plate"><div class="quick"><div class="q">QUICK SHOP</div><div class="a">ADD TO CART</div></div></div><p>Lorem Ipsum is simply dummy text of the</p><div class="price">$25.542</div></div>
  <div class="card"><div class="pic t-hooks" role="img" aria-label="Seahorse wall hooks"><span class="tag new">New</span></div><p>Lorem Ipsum is simply dummy text of the</p><div class="price">$11.24</div></div>
  <div class="card"><div class="pic t-cups" role="img" aria-label="Chevron patterned tumblers with straws"></div><p>Lorem Ipsum is simply dummy text of the</p><div class="price">$54.21</div></div>
  <div class="card"><div class="pic t-band" role="img" aria-label="Charm bracelet on a plate"><span class="tag sale">Sale</span></div><p>Lorem Ipsum is simply dummy text of the</p><div class="price">$32.4710</div></div>

  <div class="card"><div class="pic t-basket" role="img" aria-label="Christmas gift basket with baubles"><span class="tag best">Best</span></div><p>Lorem Ipsum is simply dummy text of the</p><div class="price">$25.542</div></div>
  <div class="card"><div class="pic t-rings" role="img" aria-label="Gold rings on an envelope"></div><p>Lorem Ipsum is simply dummy text of the</p><div class="price">$11.24</div></div>
  <div class="card"><div class="pic t-flower" role="img" aria-label="White ceramic flower vase"><span class="tag sale">Sale</span></div><p>Lorem Ipsum is simply dummy text of the</p><div class="price">$54.21</div></div>
  <div class="card"><div class="pic t-eggs" role="img" aria-label="Eggs in a straw nest"></div><p>Lorem Ipsum is simply dummy text of the</p><div class="price">$32.4710</div></div>

  <div class="card"><div class="pic t-band" role="img" aria-label="Charm bracelet on a plate"><span class="tag sale">Sale</span></div><p>Lorem Ipsum is simply dummy text of the</p><div class="price">$25.542</div></div>
  <div class="card"><div class="pic t-hooks" role="img" aria-label="Seahorse wall hooks"></div><p>Lorem Ipsum is simply dummy text of the</p><div class="price">$11.24</div></div>
  <div class="card"><div class="pic t-cups" role="img" aria-label="Chevron patterned tumblers with straws"></div><p>Lorem Ipsum is simply dummy text of the</p><div class="price">$54.21</div></div>
  <div class="card"><div class="pic t-band" role="img" aria-label="Charm bracelet on a plate"><span class="tag new">New</span></div><p>Lorem Ipsum is simply dummy text of the</p><div class="price">$32.4710</div></div>
</div>

<!-- about -->
<div class="abs sec-title" style="left:230px;top:899px">What we do?</div>
<div class="abs about-img" role="img" aria-label="Handmade greeting card with floral panels"></div>
<div class="abs about">
  <h3>Gift Baskets &amp; Hampers Delivered throughout Australia.</h3>
  <p>Send Gifts to Sydney NSW, Brisbane QLD, Melbourne VIC, Canberra ACT, Adelaide SA, Perth WA, Darwin NT, Hobart TAS and more via our online store, providing our customers with Gift Baskets and Hampers Australia Wide.</p>
  <p>Searching for that Perfect Gift? We provide a great range in our online gift shop! As Australia's premier Gift Basket and Hamper network we can offer you an enormous and exclusive range of special gifts sent at great prices.</p>
  <p>We deliver all sorts of gifts including Gourmet Hampers, Fruit Baskets, Delicious Cakes, Live Plants, Herbs and Flowers, Cuddly Teddies in all shapes and sizes, Lollies, Chocolate and presents for all occasions, such as birthdays, anniversaries and even special holiday seasons throughout the year.<br>All our gifts can be ordered online 24 hours a day for Delivery Australia wide.<br>So, when it comes to buying and sending gifts online, you can rely on the experts at parcelnook.com.au!</p>
</div>

<!-- footer -->
<footer class="abs footer"></footer>
<div class="abs flinks">Home <i>-</i> About us <i>-</i> Links <i>-</i> Search site <i>-</i> Privacy Policy <i>-</i> Terms &amp; Condition <i>-</i> Contact us</div>
<div class="abs copy">© 2014 Copyright &nbsp;All Rights Reserved parcelnook.com.au</div>
<div class="abs pay"><span></span><span></span><span></span><span></span><span></span></div>

</body>
</html>
```